Exclusive Offer Verbalis December 2022

A design that includes the company logo company and the text set out below. It could be a season design (winter design). it is a short promo to be sent by email. It should express that the promotion is on translation services.

Title: ESPECIAL DICIEMBRE

Information:

10% Descuento del 13 al 16 de diciembre
8% Después del 13 y hasta el 24 de diciembre

En contenidos web, materiales publicitarios, catàlogos, textos legales, manuales y más.

+30 años de experiencia, ISO 17100, traductores nativos

Target Market(s)

B2B Spain - any company that needs translation services

Industry/Entity Type

Services and Translation

Requirements
Must have
• Please take into account our corporate style guide attached
Nice to have
• A design that suggests a special offer from a serious, professional, technological and solid translation company.
Should not have
• Typical Christmas stationery, colours that don't fit into our company design trend.

```html
<!DOCTYPE html>
<html lang="es">
<head>
<meta charset="utf-8">
<title>Especial Diciembre – Verbalis</title>
<link href="https://fonts.googleapis.com/css2?family=Montserrat:ital,wght@0,400;0,500;0,600;0,700;1,600&family=Oswald:wght@400;500&display=swap" rel="stylesheet">
<style>
  :root {
    --sky-top: #0a5aa6;
    --sky-bottom: #0a8ad8;
    --orange-light: #f4b400;
    --orange-dark: #f08a00;
    --white: #ffffff;
    --navy: #1f3f75;
    --footer: #4d6c96;
  }
  * { margin: 0; padding: 0; box-sizing: border-box; }
  html, body { width: 738px; height: 1200px; overflow: hidden; }
  body { font-family: "Montserrat", sans-serif; color: var(--white); }
  .promo {
    position: relative; width: 738px; height: 1200px; overflow: hidden;
    background: linear-gradient(180deg, var(--sky-top) 0%, var(--sky-bottom) 82%);
  }
  .ornament { position: absolute; left: 0; top: 0; }
  .ornament-title {
    position: absolute; left: 0; width: 738px; top: 118px;
    text-align: center; font-weight: 700; font-size: 37px; line-height: 39px;
    text-shadow: 2px 2px 3px rgba(120,60,0,0.55);
  }
  .centered { position: absolute; left: 0; width: 738px; text-align: center; }
  .season { top: 292px; font-family: "Oswald", sans-serif; font-weight: 400; font-size: 44px; line-height: 54px; letter-spacing: -0.5px; }
  .discount { font-family: "Oswald", sans-serif; font-weight: 400; font-size: 56px; line-height: 60px; }
  .discount-main { top: 368px; }
  .discount-second { top: 477px; }
  .dates { font-size: 21px; font-weight: 500; line-height: 26px; }
  .dates-main { top: 431px; }
  .dates-second { top: 540px; }
  .services {
    position: absolute; left: 69px; top: 592px; width: 600px; height: 92px;
    border: 3px solid var(--white); border-radius: 46px;
    background: linear-gradient(180deg, var(--orange-light), var(--orange-dark));
    display: flex; align-items: center; justify-content: center; text-align: center;
    font-size: 21px; font-weight: 600; line-height: 25px;
  }
  .credentials { top: 694px; font-size: 23px; font-weight: 600; font-style: italic; line-height: 29px; }
  .forest {
    position: absolute; left: 122px; top: 764px; width: 474px; height: 216px;
    background: linear-gradient(180deg, rgba(255,255,255,0) 0%, rgba(255,255,255,0.55) 60%, rgba(255,255,255,0.9) 100%);
  }
  .ground { position: absolute; left: 0; top: 970px; }
  .brand {
    position: absolute; left: 226px; top: 1010px; display: flex; align-items: center; gap: 14px;
    color: var(--navy);
  }
  .brand-mark { width: 62px; height: 62px; background: var(--navy); }
  .brand-name { font-weight: 700; font-size: 34px; letter-spacing: 2px; line-height: 36px; }
  .brand-tagline { font-weight: 700; font-size: 11.5px; line-height: 16px; margin-top: 8px; }
  .social { position: absolute; left: 0; top: 1102px; width: 738px; display: flex; justify-content: center; gap: 8px; }
  .social span {
    width: 34px; height: 34px; border-radius: 50%;
    background: linear-gradient(180deg, var(--orange-light), var(--orange-dark));
    box-shadow: 0 0 0 2px var(--white), 0 0 0 3px #d9d9d9;
  }
  .contact {
    position: absolute; left: 0; top: 1152px; width: 738px; height: 48px;
    background: var(--footer); display: flex; align-items: center; justify-content: center;
    font-size: 11px; gap: 17px; white-space: nowrap;
  }
  .contact b { font-weight: 700; }
</style>
</head>
<body>
<main class="promo">
  <svg class="ornament" width="738" height="300" viewBox="0 0 738 300" aria-hidden="true">
    <defs>
      <linearGradient id="ballFill" x1="0" y1="0" x2="0" y2="1">
        <stop offset="0" stop-color="#f4b400"/>
        <stop offset="1" stop-color="#f08a00"/>
      </linearGradient>
    </defs>
    <line x1="369" y1="0" x2="369" y2="43" stroke="#f4a800" stroke-width="2"/>
    <circle cx="369" cy="160" r="116" fill="none" stroke="#f4a800" stroke-width="2"/>
    <circle cx="369" cy="160" r="110" fill="url(#ballFill)"/>
  </svg>
  <h1 class="ornament-title">Especial<br>Diciembre</h1>

  <p class="centered season">Promoción de Temporada</p>
  <p class="centered discount discount-main">10% DESCUENTO</p>
  <p class="centered dates dates-main">del 13 al 16 de diciembre</p>
  <p class="centered discount discount-second">8%</p>
  <p class="centered dates dates-second">del 13 y hasta el 24 de diciembre</p>

  <div class="services">En contenidos web, materiales publicitarios,<br>catálogos, textos legales, manuales y más.</div>

  <p class="centered credentials">+30 años de experiencia, ISO 17100,<br>traductores nativos</p>

  <div class="forest" role="img" aria-label="Ilustración de pinos nevados blancos sobre el horizonte"></div>

  <svg class="ground" width="738" height="182" viewBox="0 0 738 182" aria-hidden="true">
    <path d="M0 10 Q369 -6 738 10 L738 182 L0 182 Z" fill="#ffffff"/>
  </svg>

  <div class="brand">
    <span class="brand-mark"></span>
    <div>
      <div class="brand-name">VERBALIS</div>
      <div class="brand-tagline">TRADUCCIÓN Y DOCUMENTACIÓN<br>MULTILINGÜE</div>
    </div>
  </div>

  <nav class="social" aria-label="Redes sociales">
    <span></span><span></span><span></span><span></span>
  </nav>

  <footer class="contact">
    <span><b>P:</b> +34 91 000 00 00</span><span>|</span>
    <span><b>E:</b> hola@verbalis.es</span><span>|</span>
    <span><b>W:</b> www.verbalis.es</span><span>|</span>
    <span>C/ Ejemplo 12, 3 º - 4 ª, 08000 Barcelona</span>
  </footer>
</main>
</body>
</html>
```